Book Flyer

I want a flyer that we can use to promote this book to educators and to leaders....below is a sample flyer but I want something bold and creative and different from this....it can be completely different from what is attached. I want to be a WOW to increase sales. Please include pic of book and how folks can get a copy....I've given you a few pics but please be creative ....looking for a wow.

```html
<!DOCTYPE html>
<html lang="en">
<head>
<meta charset="utf-8">
<title>Purposeful Excellence – Book Flyer</title>
<link rel="stylesheet" href="https://fonts.googleapis.com/css2?family=Roboto:wght@300;400;500;700;900&family=Roboto+Condensed:wght@300;400;700&display=swap">
<style>
  :root{
    --ink:#000000;
    --title-blue:#1479c0;
    --band-blue:#1a7dc2;
    --orange:#f07b1a;
    --red:#e84142;
    --white:#ffffff;
    --soft-grey:#d6d6d6;
    --dark-text:#161616;
    --stage:#e2e2e2;
  }
  html,body{margin:0;padding:0;width:1200px;height:1200px;overflow:hidden;background:var(--stage);}
  .flyer{
    position:absolute;left:180px;top:57px;width:988px;height:1278px;
    transform:scale(0.85);transform-origin:0 0;
    font-family:"Roboto",Arial,sans-serif;color:var(--white);
    box-shadow:0 12px 30px rgba(0,0,0,.35);overflow:hidden;
  }
  .flyer__shapes{position:absolute;inset:0;}
  .title{position:absolute;left:74px;margin:0;line-height:1;white-space:nowrap;}
  .title--main{top:52px;font-size:90px;font-weight:900;letter-spacing:-2px;color:var(--title-blue);}
  .title--sub{top:132px;font-size:86px;font-weight:300;color:var(--orange);letter-spacing:-1px;}
  .intro{
    position:absolute;left:80px;top:212px;width:514px;margin:0;
    font-family:"Roboto Condensed",Arial,sans-serif;font-weight:300;
    font-size:18.5px;line-height:23.2px;text-align:justify;color:var(--soft-grey);
  }
  .strategies-head{position:absolute;right:406px;top:376px;text-align:right;color:var(--red);margin:0;}
  .strategies-head span{display:block;line-height:1.12;}
  .strategies-head .big{font-size:46px;font-weight:700;}
  .strategies-head .mid{font-size:35px;font-weight:700;}
  .strategies-head .small{font-size:27px;font-weight:500;}
  .strategy-rule{position:absolute;left:43px;top:516px;width:9px;height:328px;background:var(--ink);border-radius:3px;}
  .strategy{position:absolute;left:77px;width:340px;}
  .strategy h3{margin:0;font-family:"Roboto Condensed",Arial,sans-serif;font-weight:700;font-size:34px;line-height:1;color:var(--white);}
  .strategy p{margin:8px 0 0;font-weight:300;font-size:16px;line-height:19.5px;color:var(--dark-text);}
  .strategy cite{display:block;font-style:normal;font-weight:500;font-size:16px;line-height:19.5px;color:var(--dark-text);}
  .strategy--equity{top:514px;}
  .strategy--change{top:642px;}
  .strategy--communication{top:752px;}
  .book-cover{
    position:absolute;left:43px;top:872px;width:175px;height:244px;
    background:linear-gradient(180deg,#1f3a6b 0%,#2a4a80 48%,#e0393a 49%,#e0393a 72%,#ffffff 73%,#ffffff 100%);
    box-shadow:4px 6px 10px rgba(0,0,0,.45);
  }
  .about{position:absolute;left:286px;top:940px;width:620px;}
  .about h2{margin:0;font-size:42px;font-weight:900;line-height:1.1;color:var(--ink);}
  .about p{margin:4px 0 0;font-size:18px;font-weight:500;line-height:23.3px;color:var(--ink);}
  .contact{
    position:absolute;left:0;right:0;top:1190px;margin:0;text-align:center;
    font-size:35px;font-weight:500;color:var(--band-blue);
  }
</style>
</head>
<body>
<main class="flyer">
  <svg class="flyer__shapes" viewBox="0 0 988 1278" width="988" height="1278" aria-hidden="false">
    <defs>
      <linearGradient id="photoTone" x1="0" y1="0" x2="0.6" y2="1">
        <stop offset="0" stop-color="#6f93bd"/>
        <stop offset="0.35" stop-color="#8a95a3"/>
        <stop offset="0.7" stop-color="#3a3d46"/>
        <stop offset="1" stop-color="#23252c"/>
      </linearGradient>
    </defs>
    <rect class="bg-ink" x="0" y="0" width="988" height="1278" fill="var(--ink)"/>
    <polygon class="author-photo" role="img" aria-label="Photo of the author in a dark suit reading the book outside a glass building" points="614,0 988,0 988,1032 432,811 614,670" fill="url(#photoTone)"/>
    <polygon class="red-wedge" points="0,378 614,670 0,1132" fill="var(--red)"/>
    <polygon class="blue-band" points="432,811 988,1032 988,1150 0,1150 0,1132" fill="var(--band-blue)"/>
    <rect class="footer-band" x="0" y="1150" width="988" height="128" fill="var(--ink)"/>
  </svg>

  <h1 class="title title--main">PURPOSEFUL</h1>
  <p class="title title--sub">EXCELLENCE</p>

  <p class="intro">Purposeful Excellence is a book written for all leaders. Dr. Marcus Hale speaks from real life experiences that are relatable and from the heart. His leadership steps have helped him develop into one of the most accomplished administrative leaders in the country. The three specific strategies outlined in this book will transform your leadership skills and help you stay on track to ensure success.</p>

  <h2 class="strategies-head">
    <span class="big">3 Fundamental</span>
    <span class="mid">Strategies</span>
    <span class="small">That Drive Leadership</span>
  </h2>

  <div class="strategy-rule"></div>

  <section class="strategy strategy--equity">
    <h3>1. EQUITY</h3>
    <p>Fariness does not mean everyone gets the same. Fairness means everyone gets what they need.</p>
    <cite>-Ray Morrow</cite>
  </section>
  <section class="strategy strategy--change">
    <h3>2. CHANGE</h3>
    <p>If you do not change direction, you may end up where you are heading.</p>
    <cite>-Lin Tao</cite>
  </section>
  <section class="strategy strategy--communication">
    <h3>3. COMMUNICATION</h3>
    <p>The single biggest problem in communication is the illusinon that is has taken place.</p>
    <cite>-Lin Tao</cite>
  </section>

  <div class="book-cover" role="img" aria-label="Front cover of the book Purposeful Excellence with rising arrows"></div>

  <section class="about">
    <h2>About Dr. Hale</h2>
    <p>Distinguished as a vibrant, visionary, and innovative leader who recognizes that humility is the most important trait a leader can possess. Dr. Hale uses his prior experiences in business, education, and nonprofit to assist organization leaders from all industries build internal leadership capacity, including strategy &amp; talent management and development to maximize organizational potential and success.</p>
  </section>

  <p class="contact">For more info contact Us : info@thehalegroup.com</p>
</main>
</body>
</html>
```